Brilliant Design Needed For Stand Up Pouch - Drink Mix

We need a layout for our resealable stand-up pouch that holds our powered sports drink mix. Target audience is endurance athletes that enjoy marathon running, cycling, mountain biking, hiking and triathlon. Secondary audience are participants in team sports such soccer, lacrosse, football and basketball. Please review the attached project brief for full details. Thanks!

Target Market(s)

50/50 male/female, ages 20-50, USA, succesful, driven, educated. Active, healthy, athletic, outdoor lifestyle.

Industry/Entity Type

Fitness

Font styles to use
Sans Serif

Colors
33a6d7
3277b5
abd037

Requirements
Must have
• Please review the attached project brief for full details.
Nice to have
Should not have

```html
<!DOCTYPE html>
<html lang="en">
<head>
<meta charset="utf-8">
<title>Tidewell Hydration Drink Mix – Pouch Front and Back</title>
<link href="https://fonts.googleapis.com/css2?family=Montserrat:ital,wght@0,800;1,700&family=Oswald:wght@500;600&family=Source+Sans+3:wght@400;600;700&display=swap" rel="stylesheet">
<style>
  :root{
    --bg:#eeeff0;
    --navy:#0b4566;
    --navy-deep:#083552;
    --navy-light:#0f5f87;
    --cyan:#1ec3ea;
    --sky:#33a6d7;
    --blue:#3277b5;
    --lime:#abd037;
    --white:#ffffff;
    --silver:#d9dadc;
    --label:#c9cacb;
  }
  *{box-sizing:border-box;margin:0;padding:0}
  html,body{width:1200px;height:927px;overflow:hidden;background:var(--bg)}
  .canvas{position:relative;width:1200px;height:927px;font-family:"Source Sans 3",sans-serif}
  .pouch{position:absolute;top:103px;width:501px;height:714px;border-radius:6px;
    background:radial-gradient(ellipse at 45% 35%,var(--navy-light) 0%,var(--navy) 55%,var(--navy-deep) 100%);overflow:hidden}
  .pouch--front{left:70px}
  .pouch--back{left:619px}
  .abs{position:absolute}

  /* front */
  .side-band{left:0;top:0;width:154px;height:100%;background:linear-gradient(90deg,var(--silver),var(--white) 60%,#f4f5f6)}
  .side-title{left:38px;top:688px;transform-origin:0 0;transform:rotate(-90deg);
    font-family:"Montserrat",sans-serif;font-weight:800;font-size:84px;letter-spacing:1px;color:var(--cyan);white-space:nowrap;line-height:1}
  .side-sub{left:110px;top:688px;transform-origin:0 0;transform:rotate(-90deg);
    font-family:"Montserrat",sans-serif;font-style:italic;font-weight:700;font-size:29px;letter-spacing:1px;color:var(--navy);white-space:nowrap;line-height:1}
  .side-rules{left:122px;top:347px;width:8px;height:76px;border-left:1px solid var(--navy);border-right:1px solid var(--navy)}
  .brand{font-family:"Oswald",sans-serif;font-weight:600;color:var(--cyan);letter-spacing:3px;text-align:center;line-height:1}
  .front .brand{left:154px;width:347px;top:208px;font-size:36px}
  .product{left:154px;width:347px;text-align:center;top:286px;font-family:"Oswald",sans-serif;font-weight:600;font-size:60px;color:var(--white);line-height:1;letter-spacing:-1px}
  .tagline{left:154px;width:347px;text-align:center;top:348px;font-family:"Oswald",sans-serif;font-weight:600;font-size:21px;color:var(--cyan);letter-spacing:.5px}
  .flavor{left:200px;top:588px;background:var(--lime);color:var(--navy-deep);border-radius:4px;padding:2px 8px;font-family:"Oswald",sans-serif;font-weight:500;font-size:9.5px}
  .claims{left:200px;top:612px;list-style:none;font-family:"Oswald",sans-serif;color:var(--white);font-size:11px;line-height:18px}
  .claims li::before,.features li::before{content:"";display:inline-block;width:7px;height:7px;background:var(--white);margin-right:7px;vertical-align:1px}
  .yield{left:200px;top:660px;font-family:"Oswald",sans-serif;font-weight:600;font-size:15px;color:var(--sky);line-height:1.1}
  .weight{left:200px;top:677px;font-family:"Oswald",sans-serif;font-weight:600;font-size:17px;color:var(--white)}

  /* back */
  .back .brand{left:0;width:100%;top:204px;font-size:36px}
  .section-title{left:0;width:100%;text-align:center;top:262px;font-family:"Oswald",sans-serif;font-weight:600;font-size:21px;color:var(--cyan)}
  .mix-visual{left:62px;top:295px;width:114px;height:120px;border-radius:4px;background:linear-gradient(160deg,#f6f7f8,#e3e6e9)}
  .mix-table{left:183px;top:295px;width:262px;border-collapse:collapse;border:1px solid rgba(255,255,255,.6);font-family:"Oswald",sans-serif;font-weight:500;color:var(--white);font-size:11.5px}
  .mix-table th{background:var(--sky);height:28px;text-align:left;padding-left:14px;font-weight:500}
  .mix-table td{height:30px;padding-left:14px;border-top:1px solid rgba(255,255,255,.5);border-left:1px solid rgba(255,255,255,.5)}
  .mix-table td:first-child{border-left:0}
  .mix-table th+th{border-left:1px solid rgba(255,255,255,.5)}
  .mix-table tr:nth-child(2) td{border-top:0;height:32px;padding-top:4px}
  .h-small{font-weight:700;font-size:9.5px;color:var(--sky);letter-spacing:.3px}
  .directions{left:59px;top:436px;width:260px;color:var(--white);font-size:10px;line-height:1.3}
  .features-title{left:59px;top:486px}
  .features{left:59px;top:503px;list-style:none;color:var(--white);font-weight:700;font-size:10px;line-height:12.5px}
  .blurb{left:59px;top:571px;width:245px;color:var(--white);font-size:7.4px;line-height:1.35}
  .dist{left:59px;top:641px;color:var(--white);font-weight:700;font-size:9.5px;line-height:1.35}
  .label-area{left:328px;top:434px;width:116px;height:209px;background:var(--label)}
  .badges{left:281px;top:654px;display:flex;gap:8px}
  .badge{width:35px;height:35px;border-radius:50%;border:1.5px solid var(--white)}
</style>
</head>
<body>
<main class="canvas">

  <section class="pouch pouch--front front" aria-label="Pouch front">
    <div class="abs side-band"></div>
    <div class="abs side-title">HYDRATION</div>
    <div class="abs side-sub">ULTRA FORMULA</div>
    <div class="abs side-rules"></div>
    <div class="abs brand">TIDEWELL</div>
    <h1 class="abs product">DRINK MIX</h1>
    <p class="abs tagline">PACE EVERY MILE</p>
    <span class="abs flavor">Lemon-Lime with other natural flavors</span>
    <ul class="abs claims">
      <li>Advanced Hydration System</li>
      <li>Recommended For 3+ Hour Workouts</li>
    </ul>
    <p class="abs yield">MAKES 27,12 FL OZ SERVINGS</p>
    <p class="abs weight">NET WT. 15.5 OZ (440G)</p>
  </section>

  <section class="pouch pouch--back back" aria-label="Pouch back">
    <div class="abs brand">TIDEWELL</div>
    <h2 class="abs section-title">MIXING INSTRUCTIONS</h2>
    <div class="abs mix-visual" role="img" aria-label="Illustration of a hand pouring a scoop of powder into a water bottle"></div>
    <table class="abs mix-table">
      <tr><th>TO MAKE</th><th>TIDEWELL MIX</th><th>COLD WATER</th></tr>
      <tr><td>12 FL OZ</td><td>1 Scoop</td><td>12 FL OZ</td></tr>
      <tr><td>24 FL OZ</td><td>2 Scoops</td><td>24 FL OZ</td></tr>
      <tr><td>1 Gallon</td><td>27 Scoops</td><td>1 Gallon</td></tr>
    </table>
    <div class="abs directions">
      <p class="h-small">DIRECTIONS:</p>
      <p>Pour Tidewell drink mix powder into a bottle. Add water. Shake until powder completely dissolves.</p>
    </div>
    <p class="abs h-small features-title">TIDEWELL ULTRA FORMULA HAS:</p>
    <ul class="abs features">
      <li>250 calories per Serving</li>
      <li>Carbohydrates for sustained energy</li>
      <li>Complete Electrolytes</li>
      <li>Vitamin C</li>
      <li>Caffeine</li>
    </ul>
    <p class="abs blurb"><b>Tidewell ULTRA Formula</b> is designed for long-lasting workouts of <b>3-hours</b> or more. This formula is designed to support marathons and ultra-marathons, long-course triathlons, cycling and mountain biking, and hiking. With increased levels of carbohydrates and electrolytes, along with Vitamin C and caffeine, Tidewell ENDURANCE Formula is a great choice for extreme athletes pushing their limits.</p>
    <div class="abs dist">
      <p class="h-small">DISTRIBUTED BY</p>
      <p>TIDEWELL ENDURANCE WORKS,<br>LLC, DUNMORE, MA 01900<br>WWW.TIDEWELL.EXAMPLE</p>
    </div>
    <div class="abs label-area"></div>
    <div class="abs badges" aria-label="Dietary certification badges">
      <span class="badge"></span><span class="badge"></span><span class="badge"></span><span class="badge"></span>
    </div>
  </section>

</main>
</body>
</html>
```